Startseite gestalten!
Zielgruppe
20 - 45 Jahre alt, legt Wert auf Mode usw.
Hallo,
ich suche jemanden, der mir die Startseite von R&T kavamode (www.rt-kavamode-example.com) chic gestalten kann.
Die Elemente, die jetzt drauf sind sollen bleiben... es geht nur noch um die Gestaltung.
Also Video, Blog und 2 "Werbeflächen" sollen bleiben....
Ebenso die Grundfarbgestaltung usw.
Soll halt schön in die restl. Seite passen.
Freue mich auf die Entwürfe!

```html
<!DOCTYPE html>
<html lang="de">
<head>
<meta charset="utf-8">
<title>R&amp;T kavamode – Startseite</title>
<link rel="stylesheet" href="https://fonts.googleapis.com/css2?family=Noto+Sans:wght@400;700&display=swap">
<style>
  :root {
    --page-bg: #ffffff;
    --kids-top: #ea78a8;
    --kids-bottom: #c51f60;
    --men-top: #2a8bd6;
    --men-bottom: #d6ebf9;
    --club-top: #86b6e2;
    --club-bottom: #d8eaf7;
    --acc-top: #2160bb;
    --acc-bottom: #120d55;
    --white: #ffffff;
    --ink: #111111;
    --club-blue: #3d9ad8;
    --photo-kids: linear-gradient(180deg, #d45e8d 0%, #2b3358 100%);
    --photo-men: linear-gradient(180deg, #4f9bd8 0%, #8a6a4c 100%);
    --photo-club: linear-gradient(180deg, #8fbbe4 0%, #2c3040 100%);
    --photo-acc: linear-gradient(180deg, #2d63b8 0%, #8f7257 100%);
  }
  * { box-sizing: border-box; margin: 0; padding: 0; }
  html, body {
    width: 1200px; height: 2400px; overflow: hidden;
    background: var(--page-bg);
    font-family: "Noto Sans", Verdana, sans-serif;
  }
  .teaser {
    position: absolute; left: 30px; width: 1140px; height: 436px; overflow: hidden;
  }
  .teaser--kids { top: 40px; background: linear-gradient(180deg, var(--kids-top), var(--kids-bottom)); color: var(--white); }
  .teaser--men { top: 515px; background: linear-gradient(180deg, var(--men-top), var(--men-bottom)); color: var(--ink); }
  .teaser--club { top: 1009px; background: linear-gradient(180deg, var(--club-top), var(--club-bottom)); color: var(--ink); }
  .teaser--acc { top: 1489px; background: linear-gradient(180deg, var(--acc-top), var(--acc-bottom)); color: var(--white); }

  .teaser__photo {
    position: absolute; top: 0; bottom: 0; left: 0; width: 540px;
  }
  .teaser--kids .teaser__photo { background: var(--photo-kids); }
  .teaser--men .teaser__photo { background: var(--photo-men); }
  .teaser--club .teaser__photo { background: var(--photo-club); }
  .teaser--acc .teaser__photo { background: var(--photo-acc); }

  .brand {
    position: absolute; left: 643px; top: 18px; width: 400px;
    text-align: center; font-weight: 400; line-height: 1;
  }
  .brand__name { display: block; font-size: 150px; letter-spacing: 4px; }
  .brand__tag { display: block; font-size: 26px; margin-top: 2px; }
  .teaser--kids .brand, .teaser--acc .brand { color: var(--white); }
  .teaser--men .brand, .teaser--club .brand { color: var(--ink); }

  .teaser__title { position: absolute; font-weight: 700; font-size: 36px; line-height: 1.45; }
  .teaser__text { position: absolute; font-size: 24px; }
  .teaser__link {
    position: absolute; right: 53px; font-weight: 700; font-size: 23px;
    display: flex; align-items: center; gap: 10px;
  }
  .teaser__link svg { width: 14px; height: 20px; }

  .teaser--kids .teaser__title { left: 480px; top: 268px; }
  .teaser--kids .teaser__text { left: 545px; top: 320px; }
  .teaser--kids .teaser__link { top: 378px; }

  .teaser--men .teaser__title { left: 600px; width: 500px; top: 256px; text-align: center; }
  .teaser--men .teaser__link { top: 376px; }

  .teaser--club .teaser__title { left: 600px; width: 520px; top: 262px; text-align: center; color: var(--club-blue); }
  .teaser--club .teaser__link { top: 378px; color: var(--club-blue); }

  .teaser--acc .teaser__title { left: 560px; top: 268px; }
  .teaser--acc .teaser__text { left: 610px; top: 320px; }
  .teaser--acc .teaser__link { top: 376px; }
</style>
</head>
<body>
<main class="teasers">

  <section class="teaser teaser--kids">
    <div class="teaser__photo" role="img" aria-label="Foto: Kind mit Polohelm und Poloschläger im dunkelblauen Shirt"></div>
    <div class="brand"><span class="brand__name">R&amp;T</span><span class="brand__tag">kavamode</span></div>
    <h2 class="teaser__title">Shirts für unsere Kids</h2>
    <p class="teaser__text">Lorem ipsum dolor sit amet consetetur</p>
    <a class="teaser__link">Zu den Shirts
      <svg viewBox="0 0 14 20"><path d="M3 2l8 8-8 8" fill="none" stroke="currentColor" stroke-width="4"/></svg></a>
  </section>

  <section class="teaser teaser--men">
    <div class="teaser__photo" role="img" aria-label="Foto: Polospieler im schwarzen Teamshirt mit seinem Pferd"></div>
    <div class="brand"><span class="brand__name">R&amp;T</span><span class="brand__tag">kavamode</span></div>
    <h2 class="teaser__title">Herren 2008<br>Original Team Shirt</h2>
    <a class="teaser__link">Jetzt bestellen
      <svg viewBox="0 0 14 20"><path d="M3 2l8 8-8 8" fill="none" stroke="currentColor" stroke-width="4"/></svg></a>
  </section>

  <section class="teaser teaser--club">
    <div class="teaser__photo" role="img" aria-label="Foto: Drei Spieler in schwarzen Teamshirts vor blauem Himmel"></div>
    <div class="brand"><span class="brand__name">R&amp;T</span><span class="brand__tag">kavamode</span></div>
    <h2 class="teaser__title">Das Original Teamshirts<br>des Isartal Polo Clubs</h2>
    <a class="teaser__link">Jetzt bestellen
      <svg viewBox="0 0 14 20"><path d="M3 2l8 8-8 8" fill="none" stroke="currentColor" stroke-width="4"/></svg></a>
  </section>

  <section class="teaser teaser--acc">
    <div class="teaser__photo" role="img" aria-label="Produktfoto: Teddybär im Shirt, Trinkbecher und schwarze Kappe"></div>
    <div class="brand"><span class="brand__name">R&amp;T</span><span class="brand__tag">kavamode</span></div>
    <h2 class="teaser__title">Accessoires</h2>
    <p class="teaser__text">Lorem ipsum dolor sit amet consetetur</p>
    <a class="teaser__link">Zu den Accessoires
      <svg viewBox="0 0 14 20"><path d="M3 2l8 8-8 8" fill="none" stroke="currentColor" stroke-width="4"/></svg></a>
  </section>

</main>
</body>
</html>
```